Business card for new business - financial management

I need a business card designed for my new business. I'm the owner / sole trader of QVB Consulting, which provides financial management services for Government. I'd like the design to incorporate the attached business name and colours. The design should include colour and not be too way out - it needs to look at home in a government environment.
Details to be included on the card are:
QVB Consulting
Miriam Haskett
0400 386 924
miriamrhaskett@fernmail.example
47 Pallister Crescent, Curtin ACT 2605
Single or double sided designs would be good.
Employees at Australian Federal Government agencies
Government

```html
<!DOCTYPE html>
<html lang="en">
<head>
<meta charset="utf-8">
<title>QVB Consulting – Business Card</title>
<link rel="stylesheet" href="https://fonts.googleapis.com/css2?family=Source+Sans+3:ital,wght@0,300;0,400;1,300&display=swap">
<style>
  :root {
    --brand-blue: #2358c5;
    --brand-aqua: #92f0df;
    --brand-teal: #1a5a6b;
    --paper: #ffffff;
    --ink-light: #ffffff;
  }
  html, body {
    margin: 0;
    padding: 0;
    width: 1200px;
    height: 704px;
    overflow: hidden;
    background: var(--paper);
  }
  .card {
    position: relative;
    width: 1200px;
    height: 704px;
    background: var(--paper);
    font-family: "Source Sans 3", "Source Sans Pro", Arial, sans-serif;
  }
  .card__bands {
    position: absolute;
    inset: 0;
    width: 1200px;
    height: 704px;
  }
  .band--aqua { fill: var(--brand-aqua); }
  .band--blue { fill: var(--brand-blue); }

  .brand-name {
    position: absolute;
    left: 0;
    right: 0;
    top: 218px;
    margin: 0;
    text-align: center;
    font-size: 92px;
    font-weight: 400;
    line-height: 1;
    letter-spacing: 0.5px;
    color: var(--brand-blue);
  }

  .contact {
    position: absolute;
    left: 0;
    right: 0;
    top: 498px;
    margin: 0;
    text-align: center;
    color: var(--ink-light);
    font-style: normal;
  }
  .contact__line {
    display: block;
    font-size: 39px;
    font-weight: 300;
    line-height: 55px;
    white-space: nowrap;
  }
  .contact__name {
    font-weight: 400;
  }
  .contact__role {
    font-style: italic;
    font-weight: 300;
    font-size: 35px;
  }
</style>
</head>
<body>
  <main class="card">
    <svg class="card__bands" viewBox="0 0 1200 704" aria-hidden="true">
      <path class="band--aqua" d="M0,0 H1200 V31 Q600,127 0,31 Z"/>
      <path class="band--blue" d="M0,0 H1200 V23 Q600,119 0,23 Z"/>
      <path class="band--aqua" d="M0,538 Q600,416 1200,538 V704 H0 Z"/>
      <path class="band--blue" d="M0,547 Q600,425 1200,547 V704 H0 Z"/>
    </svg>

    <h1 class="brand-name">QVB Consulting</h1>

    <address class="contact">
      <span class="contact__line"><span class="contact__name">Miriam Haskett</span> - <span class="contact__role">Owner</span></span>
      <span class="contact__line">47 Pallister Crescent, Curtin ACT 2605</span>
      <span class="contact__line">Phone: 0400 386 924 | Email: miriamrhaskett@fernmail.example</span>
    </address>
  </main>
</body>
</html>
```